Product and Services Brochure for an Oil and Gas Business

Need a brochure design for our Products and Services. I've attached expectations, Product Names, Picture link, Logo. Please ask if you have any questions.

Use Black and/or White background and related bright colors per our logo colors. Design will have black silk laminate and SPOT UV. Hence please define the respective layers and incorporate those feature in the design. Be bold, modern and unique. No cluttered designs.

Pictures link https://files.brindlevault.net/share/7QkT2mWz9pLx4RcVn8JdYe3HsGa6bUo?view=open

Logos - There are two logos that we use. One for square spaces and one for horizontal spaces

Target Market(s)

Industrial

Colors

Designer to choose colors to be used in the design.

Requirements
Must have
• Clean, uncluttered and bold design with good color pairing
Nice to have
• Pictures provided have both black and transparent backgrounds. It will be great (not sure how) but keep the background dynamic so no product pic gets lost or have weird lines
Should not have
• Too much color

```html
<!DOCTYPE html>
<html lang="en">
<head>
<meta charset="utf-8">
<title>TerraGauge Brochure Covers</title>
<link href="https://fonts.googleapis.com/css2?family=Ubuntu:wght@500;700&family=Montserrat:wght@400;500&display=swap" rel="stylesheet">
<style>
  :root {
    --stage: #e4e4e4;
    --paper: #f6f6f6;
    --ink: #2b2b2b;
    --black: #0b0b0b;
    --lime: #8dc63f;
    --lime-deep: #6aa82a;
    --steel-blue: #2f6e9e;
    --muted: #555;
  }
  * { margin: 0; padding: 0; box-sizing: border-box; }
  html, body { width: 1200px; height: 824px; overflow: hidden; background: var(--stage); }
  .spread {
    position: absolute; left: 40px; top: 32px;
    width: 1120px; height: 760px; display: flex;
    box-shadow: 0 10px 30px rgba(0,0,0,.18);
  }
  .page { position: relative; width: 560px; height: 760px; overflow: hidden; }
  .page svg.art { position: absolute; inset: 0; }
  .page--back { background: var(--paper); }
  .page--front { background: var(--black); }

  .brand { position: absolute; }
  .brand__name {
    font-family: "Ubuntu", sans-serif; font-weight: 700; color: var(--lime);
    line-height: 1;
  }
  .brand__tag {
    font-family: "Ubuntu", sans-serif; font-weight: 500;
    line-height: 1.2; margin-top: 6px;
  }
  .page--back .brand { left: 44px; top: 498px; }
  .page--back .brand__name { font-size: 38px; }
  .page--back .brand__tag { font-size: 12px; color: var(--muted); }

  .page--front .brand { left: 150px; top: 522px; }
  .page--front .brand__name { font-size: 52px; }
  .page--front .brand__tag { font-size: 15px; color: var(--steel-blue); }

  .contact {
    position: absolute; left: 44px; top: 570px;
    font-family: "Montserrat", sans-serif; font-size: 14px; line-height: 17px;
    color: var(--ink); list-style: none;
  }
  .contact li { display: flex; gap: 10px; align-items: flex-start; margin-bottom: 5px; }
  .contact svg { flex: none; margin-top: 2px; }
  .social { position: absolute; left: 44px; top: 692px; display: flex; gap: 18px; }
  .social span { width: 18px; height: 18px; background: var(--lime); display: block; }
</style>
</head>
<body>
<main class="spread">

  <section class="page page--back">
    <svg class="art" viewBox="0 0 560 760" width="560" height="760">
      <defs>
        <linearGradient id="plantTint" x1="0" y1="0" x2="1" y2="1">
          <stop offset="0" stop-color="#a9d38a"/>
          <stop offset="1" stop-color="#6f9d52"/>
        </linearGradient>
        <linearGradient id="partsTint" x1="0" y1="0" x2="1" y2="1">
          <stop offset="0" stop-color="#9be04a"/>
          <stop offset="1" stop-color="#3f8a1e"/>
        </linearGradient>
      </defs>
      <path d="M0 0 H560 V290 Q360 400 0 370 Z" fill="url(#plantTint)" role="img" aria-label="Green-tinted photo of pipeline valves and piping at an oil and gas facility"/>
      <path d="M0 372 Q360 402 560 292" fill="none" stroke="var(--lime)" stroke-width="10"/>
      <circle cx="110" cy="420" r="56" fill="#1d3f5a" stroke="var(--steel-blue)" stroke-width="8" role="img" aria-label="Product photo of a green pipeline pig cup"/>
      <circle cx="245" cy="375" r="64" fill="#7c8a94" stroke="var(--steel-blue)" stroke-width="8" role="img" aria-label="Product photo of a black inspection pig on gravel"/>
      <circle cx="398" cy="325" r="72" fill="#4a9a22" stroke="var(--lime)" stroke-width="9" role="img" aria-label="Product photo of green pipeline pig discs"/>
      <rect x="330" y="500" width="210" height="180" rx="60" fill="url(#partsTint)" role="img" aria-label="Illustration of green polyurethane pipeline pig parts"/>
      <rect x="0" y="722" width="560" height="4" fill="var(--lime)"/>
      <rect x="0" y="732" width="560" height="28" fill="var(--lime)"/>
    </svg>

    <div class="brand">
      <div class="brand__name">TerraGauge</div>
      <div class="brand__tag">Pipeline Inspection Solutions</div>
    </div>

    <ul class="contact">
      <li>
        <svg width="12" height="16" viewBox="0 0 12 16"><path d="M6 0a6 6 0 0 0-6 6c0 4 6 10 6 10s6-6 6-10a6 6 0 0 0-6-6zm0 8.5A2.5 2.5 0 1 1 6 3.5a2.5 2.5 0 0 1 0 5z" fill="var(--lime)"/></svg>
        <span>Lorem Ipsum 321<br>Dolor Sit Amet 5 - Lorem Ipsum</span>
      </li>
      <li>
        <svg width="14" height="14" viewBox="0 0 14 14"><path d="M3 0l3 3-2 2a8 8 0 0 0 5 5l2-2 3 3-2 3C6 14 0 8 0 3z" fill="var(--lime)"/></svg>
        <span>+123 456 78 - 987 654 32</span>
      </li>
      <li>
        <svg width="14" height="12" viewBox="0 0 14 12"><rect width="14" height="12" fill="var(--lime)"/><path d="M0 0l7 6 7-6" fill="none" stroke="#fff" stroke-width="1.4"/></svg>
        <span>mail@company.com</span>
      </li>
      <li>
        <svg width="14" height="14" viewBox="0 0 14 14"><circle cx="7" cy="7" r="6" fill="none" stroke="var(--lime)" stroke-width="1.6"/><path d="M1 7h12M7 1c-3 3-3 9 0 12M7 1c3 3 3 9 0 12" fill="none" stroke="var(--lime)" stroke-width="1.2"/></svg>
        <span>www.company.com</span>
      </li>
    </ul>

    <div class="social"><span></span><span></span><span></span><span></span></div>
  </section>

  <section class="page page--front">
    <svg class="art" viewBox="0 0 560 760" width="560" height="760">
      <defs>
        <linearGradient id="craneTint" x1="0" y1="0" x2="0" y2="1">
          <stop offset="0" stop-color="#b9d3ea"/>
          <stop offset=".55" stop-color="#8c8f90"/>
          <stop offset="1" stop-color="#3a3f46"/>
        </linearGradient>
      </defs>
      <rect x="0" y="0" width="560" height="760" fill="var(--paper)"/>
      <path d="M60 0 Q90 210 290 330" fill="none" stroke="var(--lime)" stroke-width="16"/>
      <path d="M80 0 H560 V560 L300 330 Q120 220 80 0 Z" fill="url(#craneTint)" role="img" aria-label="Photo of a large inspection pig being lifted by crane beside a pipeline"/>
      <path d="M0 250 Q170 300 300 330 L560 560 V760 H0 Z" fill="var(--black)"/>
      <circle cx="130" cy="330" r="62" fill="#8d9398" stroke="var(--steel-blue)" stroke-width="8" role="img" aria-label="Product photo of a pipeline pig train"/>
      <circle cx="262" cy="370" r="54" fill="#4a9a22" stroke="var(--lime)" stroke-width="8" role="img" aria-label="Product photo of green foam pipeline pigs"/>
    </svg>

    <div class="brand">
      <div class="brand__name">TerraGauge</div>
      <div class="brand__tag">Pipeline Inspection Solutions</div>
    </div>
  </section>

</main>
</body>
</html>
```